landscape and garden design business card

I would like a business card designed for my landscape and garden design company, Wrenfield Landscapes. We are located in Colorado. I would like to include our logo, contact info, and social media/web site address or QR code. Looking for an organic, flowing design that incorporates our logo.

Target Market(s)

Homeowners and businesses that need garden and landscape design

Contact Information for Business Card

Would like it to say landscape and garden design

Requirements
Must have
• Landscape and garden design

```html
<!DOCTYPE html>
<html lang="en">
<head>
<meta charset="utf-8">
<title>Wrenfield Landscapes – Business Card</title>
<link rel="stylesheet" href="https://fonts.googleapis.com/css2?family=Cormorant+Garamond:wght@600&family=Poppins:wght@400;600&display=swap">
<style>
  :root {
    --page: #ffffff;
    --teal: #0f5c4e;
    --teal-mid: #0a3f36;
    --night: #041a16;
    --sage: #c9c8b8;
    --sage-soft: #b7b6a6;
    --text-light: #f1f0ea;
    --rule: rgba(201, 200, 184, 0.45);
  }
  * { box-sizing: border-box; margin: 0; padding: 0; }
  html, body { width: 961px; height: 1200px; overflow: hidden; background: var(--page); }
  body { position: relative; font-family: "Poppins", sans-serif; }

  .card {
    position: absolute;
    left: 100px;
    width: 760px;
    height: 434px;
    overflow: hidden;
  }
  .card--front {
    top: 150px;
    background: radial-gradient(ellipse 95% 110% at 5% 10%, var(--teal) 0%, var(--teal-mid) 45%, var(--night) 85%);
  }
  .card--back {
    top: 614px;
    background: radial-gradient(ellipse 95% 110% at 98% 5%, var(--teal) 0%, var(--teal-mid) 45%, var(--night) 85%);
  }

  .brand { position: absolute; text-align: center; color: var(--sage); font-family: "Cormorant Garamond", serif; font-weight: 600; }
  .brand__disc { display: block; margin: 0 auto; background: var(--sage); }
  .brand__name { display: block; line-height: 1; }

  .card--front .brand { left: 230px; width: 300px; top: 48px; }
  .card--front .brand__disc { width: 156px; height: 110px; border-radius: 78px 78px 6px 6px; }
  .card--front .brand__name--main { font-size: 44px; margin-top: 14px; }
  .card--front .brand__name--sub { font-size: 22px; margin-top: 2px; }

  .front__web {
    position: absolute; left: 0; right: 0; top: 274px;
    text-align: center; color: var(--sage);
    font-size: 17px; letter-spacing: 2.6px;
  }
  .front__web b { font-weight: 600; }

  .meadow { position: absolute; left: 0; right: 0; bottom: 0; }
  .meadow--front { height: 111px; background: linear-gradient(to bottom, rgba(201,200,184,0) 0%, rgba(201,200,184,0.35) 70%, var(--sage-soft) 100%); }
  .meadow--back { height: 62px; background: linear-gradient(to bottom, rgba(201,200,184,0) 0%, rgba(201,200,184,0.4) 100%); }

  .card--back .brand { left: 30px; width: 300px; top: 77px; }
  .card--back .brand__disc { width: 192px; height: 136px; border-radius: 96px 96px 8px 8px; }
  .card--back .brand__name--main { font-size: 56px; margin-top: 10px; }
  .card--back .brand__name--sub { font-size: 26px; margin-top: 2px; }
  .brand__tagline {
    display: block; margin-top: 10px;
    font-family: "Poppins", sans-serif; font-weight: 400;
    font-size: 10.5px; letter-spacing: 2.4px; text-transform: uppercase;
    white-space: nowrap;
  }

  .person { position: absolute; left: 359px; top: 62px; width: 400px; }
  .person__name { font-family: "Cormorant Garamond", serif; font-weight: 600; font-size: 62px; line-height: 1; color: var(--sage); }
  .person__role { margin-top: 2px; font-size: 16px; letter-spacing: 7px; color: var(--sage); }
  .person__rule { margin-top: 8px; height: 1px; background: var(--rule); width: 320px; }

  .contact { list-style: none; margin-top: 18px; }
  .contact__item { display: flex; align-items: center; height: 31px; font-size: 17.5px; color: var(--text-light); white-space: nowrap; }
  .contact__icon { width: 20px; height: 20px; margin-right: 9px; flex: none; }

  .follow { margin-top: 16px; display: flex; align-items: center; font-size: 17.5px; color: var(--text-light); white-space: nowrap; }
  .follow__label { font-weight: 600; margin-right: 9px; }
  .follow__dot { width: 13px; height: 13px; border-radius: 50%; background: var(--sage); margin-right: 9px; flex: none; }
</style>
</head>
<body>

<section class="card card--front" aria-label="Business card front">
  <div class="brand">
    <span class="brand__disc"></span>
    <span class="brand__name brand__name--main">wrenfield</span>
    <span class="brand__name brand__name--sub">Landscapes</span>
  </div>
  <p class="front__web">www.<b>wrenfieldlandscapes</b>.com</p>
  <div class="meadow meadow--front" role="img" aria-label="Light wildflower and grass silhouettes along a pale ground line"></div>
</section>

<section class="card card--back" aria-label="Business card back">
  <div class="brand">
    <span class="brand__disc"></span>
    <span class="brand__name brand__name--main">wrenfield</span>
    <span class="brand__name brand__name--sub">Landscapes</span>
    <span class="brand__tagline">Landscape and garden design</span>
  </div>

  <div class="person">
    <h1 class="person__name">John Doe</h1>
    <p class="person__role">OWNER</p>
    <div class="person__rule"></div>

    <ul class="contact">
      <li class="contact__item">
        <svg class="contact__icon" viewBox="0 0 20 20" aria-hidden="true">
          <circle cx="10" cy="10" r="10" fill="var(--sage)"/>
          <path d="M7 5.5c.6-.3 1.1 0 1.3.5l.6 1.5c.2.4 0 .8-.3 1l-.6.5c.5 1.1 1.3 1.9 2.4 2.4l.5-.6c.3-.3.7-.4 1-.3l1.5.6c.5.2.8.7.5 1.3-.4.9-1.300 1.4-2.2 1.2-2.6-.6-4.6-2.6-5.2-5.2-.2-.9.3-1.8 1.1-2.2z" fill="var(--night)"/>
        </svg>
        (970) 555 - 0142
      </li>
      <li class="contact__item">
        <svg class="contact__icon" viewBox="0 0 20 20" aria-hidden="true">
          <circle cx="10" cy="10" r="10" fill="var(--sage)"/>
          <rect x="5" y="6.5" width="10" height="7" rx="1" fill="var(--night)"/>
          <path d="M5.5 7l4.5 3.5L14.5 7" stroke="var(--sage)" stroke-width="1" fill="none"/>
        </svg>
        info@wrenfieldlandscapes.com
      </li>
      <li class="contact__item">
        <svg class="contact__icon" viewBox="0 0 20 20" aria-hidden="true">
          <circle cx="10" cy="10" r="10" fill="var(--sage)"/>
          <circle cx="10" cy="10" r="5" fill="none" stroke="var(--night)" stroke-width="1.2"/>
          <ellipse cx="10" cy="10" rx="2.2" ry="5" fill="none" stroke="var(--night)" stroke-width="1"/>
          <path d="M5 10h10" stroke="var(--night)" stroke-width="1"/>
        </svg>
        www.wrenfieldlandscapes.com
      </li>
    </ul>

    <p class="follow">
      <span class="follow__label">Follow us on</span>
      <span class="follow__dot"></span>
      @wrenfieldlandscapes
    </p>
  </div>

  <div class="meadow meadow--back" role="img" aria-label="Faint wildflower and grass silhouettes along the bottom edge"></div>
</section>

</body>
</html>
```